Letterhead for small civil engineer company

We need bold and modern design for company letterhead in MS word. It needs to have company logo and company info. Somewhere in the upper right part of document needs to be space for "recever" and the documents starts with, example, "SUBJECT: CIVIL ENGINEER LETTERHEAD".

in the bottom part of document needs to be signature and date.

Company info: Veltrana d.o.o., Lipovac 15, Lipovac (Općina Brdarić), OIB 47396028154, www.veltrana.hr, info@veltrana.hr

Email of document sender needs to be somewhere if document, exapmle xyz@veltrana.hr

Target Market(s)

Civil engineer company and projects

Industry/Entity Type

Civil engineer

Font styles to use
Serif

Colors
F0912C
F2A743
F7CA91
FBE8D2
FDF5EE

Requirements
Must have
• Company logo and company info
Nice to have
• Moder and clean design
Should not have
• Too much details

```html
<!DOCTYPE html>
<html lang="en">
<head>
<meta charset="utf-8">
<title>Veltrana Letterhead</title>
<link href="https://fonts.googleapis.com/css2?family=Lato:wght@400;700&family=Italianno&display=swap" rel="stylesheet">
<style>
  :root {
    --orange: #e3892b;
    --grey: #6d6866;
    --ink: #383838;
    --paper: #ffffff;
    --paper-edge: #efefef;
    --backdrop: #e4e4e4;
  }
  * { margin: 0; padding: 0; box-sizing: border-box; }
  html, body {
    width: 1153px; height: 1200px; overflow: hidden;
    background: var(--backdrop);
  }
  .sheet {
    position: absolute; left: 160px; top: 17px;
    width: 1068px; height: 1494px;
    transform: scale(0.78); transform-origin: 0 0;
    background: radial-gradient(ellipse at 52% 42%, var(--paper) 0%, #f6f6f6 45%, var(--paper-edge) 100%);
    font-family: 'Lato', sans-serif; color: var(--ink);
    overflow: hidden;
  }
  .header-art, .footer-band { position: absolute; left: 0; width: 1068px; }
  .header-art { top: 0; height: 320px; }
  .footer-band { bottom: 0; height: 36px; }
  .brand-plate {
    position: absolute; left: 153px; top: 22px; width: 122px; height: 112px;
    background: var(--paper);
  }
  .brand-square {
    position: absolute; left: 12px; top: 12px; width: 98px; height: 98px;
    border: 3px solid var(--grey);
  }
  .brand-name {
    position: absolute; left: 76px; top: 140px; width: 280px;
    font-size: 40px; font-weight: 400; letter-spacing: 1px;
    color: var(--orange); text-align: center;
  }
  .recipient-block {
    position: absolute; right: 86px; top: 60px;
    text-align: right; color: #fff; font-size: 21.5px; line-height: 25.5px;
  }
  .recipient-block .label { font-weight: 700; }
  .letter { position: absolute; left: 82px; width: 904px; }
  .meta { top: 363px; font-size: 21px; line-height: 24.5px; }
  .meta .gap { height: 24px; }
  .salutation { top: 562px; font-size: 25px; font-weight: 700; }
  .body-copy { top: 622px; font-size: 19.6px; line-height: 23px; text-align: justify; }
  .body-copy p { margin-bottom: 22px; }
  .closing { top: 1036px; font-size: 20px; }
  .signature {
    top: 1085px; font-family: 'Italianno', cursive; font-size: 56px; line-height: 64px; color: #222;
  }
  .sign-date { top: 1145px; font-size: 21px; }
  .company-info {
    position: absolute; left: 82px; top: 1390px;
    font-size: 18px; line-height: 23px; color: #222;
  }
  .company-info .line-one { padding-left: 4px; }
</style>
</head>
<body>
<main class="sheet">
  <svg class="header-art" viewBox="0 0 1068 320" aria-hidden="true">
    <path fill="var(--orange)" d="M0 0H1068V148C960 200 870 212 800 210C700 206 620 178 520 128C430 86 350 60 270 48L160 48C100 56 50 74 0 95Z"/>
    <path fill="var(--grey)" d="M380 92C470 122 560 172 650 212C760 260 880 290 1068 270V155C960 207 870 221 800 219C700 215 620 187 520 137C460 110 420 98 380 92Z"/>
    <path fill="none" stroke="var(--orange)" stroke-width="8" d="M275 70C400 96 520 160 640 220C760 278 860 298 950 294"/>
    <path fill="none" stroke="var(--orange)" stroke-width="11" d="M0 110C60 88 110 80 155 77"/>
  </svg>

  <div class="brand-plate"><div class="brand-square"></div></div>
  <div class="brand-name">VELTRANA</div>

  <div class="recipient-block">
    <div class="label">RECEVER</div>
    <div>SUBJECT: CIVIL ENGINEER LETTERHEAD</div>
    <div>xyz@veltrana.hr</div>
  </div>

  <div class="letter meta">
    <div>Feb-03-2022</div>
    <div>Mr, John Doe</div>
    <div>President</div>
    <div class="gap"></div>
    <div>Harbor Corporation</div>
    <div>123 Street Name, Suite# 10</div>
    <div>City, State, 120023</div>
  </div>

  <div class="letter salutation">Dear Mr, John</div>

  <div class="letter body-copy">
    <p>Lorem ipsum dolor sit amet, consectetur adipisicing elit, sed do eiusmod tempor incididunt ut labore et dolore magna aliqua. Ut enim ad minim veniam, quis nostrud exercitation ullamco laboris nisi ut aliquip ex ea commodo consequat. Duis aute irure dolor in reprehenderit in voluptate velit esse cillum dolore eu fugiat nulla pariatur.</p>
    <p>Lorem ipsum dolor sit amet, consectetur adipisicing elit, sed do eiusmod tempor incididunt ut labore et dolore magna aliqua. Ut enim ad minim veniam, quis nostrud exercitation ullamco laboris nisi ut aliquip ex ea commodo consequat. Duis aute irure dolor in reprehenderit in voluptate velit esse cillum dolore eu fugiat nulla pariatur.</p>
    <p>Lorem ipsum dolor sit amet, consectetur adipisicing elit, sed do eiusmod tempor incididunt ut labore et dolore magna aliqua. Ut enim ad minim veniam, quis nostrud exercitation ullamco laboris nisi ut aliquip ex ea commodo consequat.</p>
    <p>Excepteur sint occaecat cupidatat non proident, sunt in culpa qui officia deserunt mollit anim id est laborum. re et dolore magnam aliquam quaerat voluptatem.</p>
  </div>

  <div class="letter closing">Regards</div>
  <div class="letter signature">Marko Lindqvist</div>
  <div class="letter sign-date">Dec-12-2024</div>

  <div class="company-info">
    <div class="line-one">Veltrana d.o.o., Lipovac 15, Lipovac (Općina Brdarić),</div>
    <div>OIB 47396028154, www.veltrana.hr, info@veltrana.hr</div>
  </div>

  <svg class="footer-band" viewBox="0 0 1068 36" aria-hidden="true">
    <polygon fill="var(--orange)" points="0,0 753,0 785,36 0,36"/>
    <polygon fill="var(--grey)" points="765,0 1068,0 1068,36 797,36"/>
  </svg>
</main>
</body>
</html>
```